Industry leading Property Management Company needs a flyer!

We need a brochure describing our fees and a basic description of what we do. This brochure will be printed, to be given to prospective clients, but we would also like an electronic version that can be downloaded from our website as a PDF. This project will be printed double sided, on standard 8.5" x 11" paper, in landscape mode, as a tri-fold brochure.

Target Market(s)

Real estate investors, but more importantly, first time investors. Many of our clients are "accidental landlords" who had their property for sale that didn't sell, so they are trying property management and rental investing for the first time. TRUST is their biggest fear

Font styles to use
Sans Serif

Requirements
Must have
• Must incorporate our logo, elements of our pricing list, and incorporate the text from our home page and "property management info" page (www.corvalinkrent.net). A word document specifying this text has been included in the project brief.
• Additionally, I am thinking this will be a simple, single piece of paper, in landscape mode, printed on both sides, in a Tri-fold. The front of the brochure will have the logo/name of the company, along with the Harbor Tenant Medals logos. I am thinking the first inside pane, when someone opens up the brochure, will have reference text #1 and #3. The 3 tiered pricing plan might occupy the 2nd and 3rd of the three panes on the inside fold. Reference text #4, 5, and 6 will occupy the next pane (see brief for handwritten layout). Then, the very back pane (when it is folded and shut) will have reference text #2 and our company contact information, plus any kind of stock photos, etc.
Nice to have
• Our main market will be first time investors, so we need to display and demonstrate relationships, and trust. We would prefer stock photos that incorporate families, children, or other images that solidify peace of mind.

```html
<!DOCTYPE html>
<html lang="en">
<head>
<meta charset="utf-8">
<title>Corvalink Tri-fold Brochure – Outside</title>
<link href="https://fonts.googleapis.com/css2?family=Montserrat:wght@600;700;800&family=Open+Sans:ital,wght@0,400;0,600;1,400&display=swap" rel="stylesheet">
<style>
  :root{
    --page:#ececec;
    --panel:#1b1c1e;
    --panel-deep:#111214;
    --blue:#1e9be0;
    --blue-dark:#0f6fae;
    --text:#c9cdd2;
    --white:#ffffff;
    --gold:#d9a93a;
  }
  *{box-sizing:border-box;margin:0;padding:0}
  html,body{width:818px;height:1200px;overflow:hidden;background:var(--page)}
  body{position:relative;font-family:"Open Sans",Arial,sans-serif}
  .brochure{
    position:absolute;left:20px;top:300px;width:778px;height:601px;
    display:grid;grid-template-columns:repeat(3,1fr);
    background:var(--panel);box-shadow:0 4px 14px rgba(0,0,0,.25);
  }
  .panel{position:relative;padding:28px 20px 22px;border-right:1px solid #2a2c30;overflow:hidden;display:flex;flex-direction:column}
  .panel:last-child{border-right:none}
  .panel::after{content:"";position:absolute;left:0;right:0;bottom:0;height:6px;background:var(--blue)}
  .section-title{
    display:flex;align-items:center;gap:7px;
    font-family:"Montserrat",Arial,sans-serif;font-weight:700;font-size:12px;
    color:var(--blue);margin:14px 0 8px;line-height:1.25;
  }
  .section-title:first-child{margin-top:0}
  .section-title svg{flex:none}
  .body-copy{font-size:8.6px;line-height:1.65;color:var(--text);margin-bottom:8px;text-align:justify}
  .accent-line{font-size:9px;font-style:italic;color:var(--blue);margin:2px 0 6px;padding-left:8px;border-left:2px solid var(--blue)}
  .web{margin-top:auto;text-align:center;font-size:8.5px;color:var(--blue);font-weight:600;padding-bottom:2px}
  .why-title{font-size:13px;color:var(--white);margin-top:16px}
  .why-title span b{color:var(--blue)}
  .divider{height:2px;background:var(--blue);width:40px;margin:4px 0 10px}
  .contact{margin-top:auto;text-align:center;padding-bottom:6px}
  .contact .section-title{justify-content:center;color:var(--white);font-size:12.5px;flex-direction:column;gap:5px;margin:0 0 6px}
  .contact-list{list-style:none;display:inline-block;text-align:left}
  .contact-list li{display:flex;align-items:center;gap:6px;font-size:8.6px;color:var(--text);margin:5px 0}
  .social{display:flex;justify-content:center;gap:7px;margin-top:9px}
  .social span{width:14px;height:14px;border-radius:50%;background:var(--blue)}
  .cover{padding:0;background:var(--panel-deep)}
  .brand{position:absolute;left:0;right:0;top:20px;display:flex;flex-direction:column;align-items:center}
  .brand-row{display:flex;align-items:center;gap:8px}
  .brand-mark{width:16px;height:16px;background:var(--blue)}
  .brand-name{font-family:"Montserrat",Arial,sans-serif;font-weight:800;font-size:19px;letter-spacing:1px;color:var(--white)}
  .brand-tag{font-size:6.5px;letter-spacing:2px;color:var(--text);margin-top:3px}
  .cover-art{position:absolute;left:0;top:72px;width:259px;height:300px}
  .cover-heading{position:absolute;left:0;right:0;top:392px;text-align:center;color:var(--white);font-family:"Montserrat",Arial,sans-serif}
  .cover-heading .lead{font-weight:600;font-size:17px}
  .cover-heading .name{font-weight:800;font-size:32px;letter-spacing:1px;margin-top:4px}
  .cover .web{position:absolute;left:0;right:0;bottom:18px}
</style>
</head>
<body>
<main class="brochure">
  <section class="panel portfolio">
    <h2 class="section-title"><svg width="14" height="14" viewBox="0 0 14 14"><circle cx="7" cy="7" r="7" fill="#1e9be0"/><path d="M3.5 7.5 7 4l3.5 3.5V11h-7z" fill="#1b1c1e"/></svg>Our Portfolio</h2>
    <p class="body-copy">Corvalink is a trusted local partner for owners of single family homes, condos, duplexes and small multi unit buildings across the valley. We care for every property as if it were our own, and we treat every owner as a long term partner.</p>
    <p class="body-copy">Our team handles marketing, screening, leasing, rent collection, inspections and repairs so first time owners can enjoy steady income without the daily stress of running a rental on their own.</p>
    <p class="body-copy">Each home we manage is inspected, priced with care and marketed to reliable tenants who stay longer and respect the property.</p>
    <h2 class="section-title"><svg width="14" height="14" viewBox="0 0 14 14"><circle cx="7" cy="7" r="7" fill="#1e9be0"/><path d="M4 7.2 6.2 9.4 10 5" stroke="#1b1c1e" stroke-width="1.6" fill="none"/></svg>Tenant Happiness and Retention</h2>
    <p class="body-copy">Happy tenants pay on time and look after your home. We answer requests quickly, schedule repairs with trusted vendors and keep every lease fair and clear.</p>
    <p class="body-copy">This simple approach lowers turnover, reduces costly vacancies and protects the value of your investment over many years.</p>
    <p class="accent-line">Fewer vacancies. Better results.</p>
    <h2 class="section-title"><svg width="14" height="14" viewBox="0 0 14 14"><circle cx="7" cy="7" r="7" fill="#1e9be0"/><path d="M4 10V7M7 10V4M10 10V6" stroke="#1b1c1e" stroke-width="1.6"/></svg>Transparency and Reporting</h2>
    <p class="body-copy">Owners get monthly statements, online access to records and a direct line to their manager whenever questions come up. Nothing is hidden and every expense is shown in writing.</p>
    <p class="web">www.corvalinkrent.net</p>
  </section>

  <section class="panel why">
    <p class="body-copy">We keep owners informed at every step, from the first showing to the final move out walk through, with clear updates by phone and email.</p>
    <p class="body-copy">Our fees are simple and listed in writing, with no hidden charges added later. You always know what you pay and why.</p>
    <p class="body-copy">We also answer every question before you sign, so you can make a confident choice for your home and your family.</p>
    <h2 class="section-title why-title"><svg width="14" height="14" viewBox="0 0 14 14"><circle cx="7" cy="7" r="7" fill="#1e9be0"/><path d="M4 7.2 6.2 9.4 10 5" stroke="#1b1c1e" stroke-width="1.6" fill="none"/></svg><span>Why choose <b>Corvalink</b> as your property management company</span></h2>
    <div class="divider"></div>
    <p class="body-copy">We combine local market knowledge with modern tools to keep your property rented and cared for. Our staff are licensed, insured and ready to help.</p>
    <p class="body-copy">Whether you are a new landlord or a seasoned investor, we give you peace of mind, honest advice and a team that truly cares.</p>
    <div class="contact">
      <h2 class="section-title"><svg width="18" height="18" viewBox="0 0 18 18"><circle cx="9" cy="9" r="9" fill="#1e9be0"/><path d="M6 5h2l1 2.5-1.3 1a6 6 0 0 0 2.8 2.8l1-1.3L14 11v2a1 1 0 0 1-1 1A8 8 0 0 1 5 6a1 1 0 0 1 1-1z" fill="#1b1c1e"/></svg>Contact Us</h2>
      <ul class="contact-list">
        <li><svg width="9" height="9" viewBox="0 0 10 10"><path d="M2 1h2l1 2.5-1 .8a5 5 0 0 0 2 2l.8-1L9 6v2a1 1 0 0 1-1 1A8 8 0 0 1 1 2a1 1 0 0 1 1-1z" fill="#1e9be0"/></svg>(208) 555 0142</li>
        <li><svg width="9" height="9" viewBox="0 0 10 10"><rect x=".5" y="2" width="9" height="6" fill="none" stroke="#1e9be0"/><path d="M.5 2 5 5.5 9.5 2" fill="none" stroke="#1e9be0"/></svg>info@corvalinkrent.net</li>
        <li><svg width="9" height="9" viewBox="0 0 10 10"><circle cx="5" cy="5" r="4.3" fill="none" stroke="#1e9be0"/><path d="M.7 5h8.6M5 .7c-2.4 2.6-2.4 6 0 8.6M5 .7c2.4 2.6 2.4 6 0 8.6" fill="none" stroke="#1e9be0" stroke-width=".8"/></svg>www.corvalinkrent.net</li>
      </ul>
      <div class="social"><span></span><span></span><span></span><span></span></div>
    </div>
  </section>

  <section class="panel cover">
    <div class="brand">
      <div class="brand-row"><span class="brand-mark"></span><span class="brand-name">CORVALINK</span></div>
      <span class="brand-tag">PROPERTY MANAGEMENT</span>
    </div>
    <svg class="cover-art" viewBox="0 0 259 300">
      <defs>
        <linearGradient id="photoTone" x1="0" y1="0" x2="1" y2="1">
          <stop offset="0" stop-color="#d7c2a3"/><stop offset="1" stop-color="#8a6a4e"/>
        </linearGradient>
      </defs>
      <polygon points="0,0 259,0 259,215 0,255" fill="url(#photoTone)" role="img" aria-label="Photo of a family with a child meeting a property manager at a kitchen table"/>
      <polygon points="0,255 259,215 259,240 0,280" fill="#1e9be0"/>
      <polygon points="0,280 259,240 259,252 0,292" fill="#0f6fae"/>
      <circle cx="42" cy="262" r="26" fill="#d9a93a" stroke="#f3d27a" stroke-width="3"/>
    </svg>
    <div class="cover-heading">
      <div class="lead">Properties Managed by</div>
      <div class="name">CORVALINK</div>
    </div>
    <p class="web">www.corvalinkrent.net</p>
  </section>
</main>
</body>
</html>
```